Want to market to schools to offer free chair massages for teacher and staff of the schools

This postcard will be mailed to all public schools in the U.S.

We want the schools to call our company to have a massage therapist provide free chair massages to the teachers and staff at their next School Improvement or Teacher Institute day.

want to make the postcard fun and inviting.

The postcard is 4 1/4" X 6"

FRONT AND BACK DESIGN.

For the back of postcard design, I have attached a template. You can use all the space except where the return label and stamp will go.

Target Market(s)

Target is schools and teachers

Industry/Entity Type

Teacher

```html
<!DOCTYPE html>
<html lang="en">
<head>
<meta charset="utf-8">
<title>Teacher Chair Massage Postcard – Back</title>
<link href="https://fonts.googleapis.com/css2?family=Arimo:ital,wght@0,400;1,400&family=Source+Sans+3:wght@700&display=swap" rel="stylesheet">
<style>
  :root {
    --stage: #000000;
    --card-blue: #1f4f9f;
    --card-teal: #4f8a86;
    --card-green: #8cb646;
    --quote-panel: rgba(34, 78, 50, 0.66);
    --figure-shade: #12383c;
    --ink-light: #ffffff;
    --ink-dark: #111111;
    --indicia-bg: #111111;
    --indicia-line: #cfcfcf;
    --label-bg: #ffffff;
  }
  * { box-sizing: border-box; margin: 0; padding: 0; }
  html, body {
    width: 1200px;
    height: 900px;
    overflow: hidden;
    background: var(--stage);
  }
  .postcard {
    position: absolute;
    left: 80px;
    top: 94px;
    width: 1012px;
    height: 728px;
    overflow: hidden;
    background: linear-gradient(110deg, var(--card-blue) 0%, var(--card-teal) 50%, var(--card-green) 100%);
  }
  .massage-scene {
    position: absolute;
    left: 0;
    top: 0;
    width: 1012px;
    height: 728px;
  }
  .testimonial {
    position: absolute;
    left: 90px;
    top: 57px;
    width: 739px;
    height: 179px;
    background: var(--quote-panel);
    color: var(--ink-light);
    font-family: "Arimo", Arial, sans-serif;
  }
  .testimonial__quote {
    position: absolute;
    left: 26px;
    top: 36px;
    font-size: 23px;
    font-style: italic;
    line-height: 34px;
  }
  .testimonial__name {
    position: absolute;
    right: 58px;
    top: 107px;
    font-size: 22px;
  }
  .testimonial__school {
    position: absolute;
    right: 58px;
    top: 137px;
    font-size: 18px;
  }
  .postage-indicia {
    position: absolute;
    left: 849px;
    top: 39px;
    width: 122px;
    height: 126px;
    background: var(--indicia-bg);
    border: 2px solid var(--indicia-line);
    outline: 2px solid var(--indicia-bg);
    color: var(--ink-light);
    font-family: "Arimo", Arial, sans-serif;
    font-size: 13px;
    line-height: 16px;
    text-align: center;
    padding-top: 20px;
  }
  .address-label {
    position: absolute;
    left: 344px;
    top: 364px;
    width: 568px;
    height: 241px;
    background: var(--label-bg);
    display: flex;
    align-items: center;
    justify-content: center;
    color: var(--ink-dark);
    font-family: "Source Sans 3", "Myriad Pro", sans-serif;
    font-weight: 700;
    font-size: 18px;
  }
</style>
</head>
<body>
  <div class="postcard">
    <svg class="massage-scene" role="img" aria-label="Silhouette of a massage therapist giving a seated chair massage to a teacher" viewBox="0 0 1012 728">
      <defs>
        <radialGradient id="seated-shade" cx="0.5" cy="0.5" r="0.5">
          <stop offset="0" stop-color="var(--figure-shade)" stop-opacity="0.75"/>
          <stop offset="0.6" stop-color="var(--figure-shade)" stop-opacity="0.45"/>
          <stop offset="1" stop-color="var(--figure-shade)" stop-opacity="0"/>
        </radialGradient>
        <radialGradient id="standing-shade" cx="0.5" cy="0.5" r="0.5">
          <stop offset="0" stop-color="var(--figure-shade)" stop-opacity="0.7"/>
          <stop offset="0.6" stop-color="var(--figure-shade)" stop-opacity="0.4"/>
          <stop offset="1" stop-color="var(--figure-shade)" stop-opacity="0"/>
        </radialGradient>
      </defs>
      <ellipse cx="220" cy="470" rx="260" ry="300" fill="url(#seated-shade)"/>
      <ellipse cx="430" cy="360" rx="200" ry="400" fill="url(#standing-shade)"/>
    </svg>

    <div class="testimonial">
      <p class="testimonial__quote">“ Each teacher was delighted to participate and couldn’t<br>&nbsp;believe the difference 10 minutes in a massage chair made”</p>
      <p class="testimonial__name">-Marisol</p>
      <p class="testimonial__school">Lakeview Public School</p>
    </div>

    <div class="postage-indicia">
      PreSort First Class<br>
      US Postage<br>
      PAID<br>
      Permit No. 2417<br>
      Fairbrook, CA
    </div>

    <div class="address-label">MAILING ADDRESS ONLY</div>
  </div>
</body>
</html>
```